Cool blackchain based app company needs a website :)

pillcheckhub.net

Kinda says it all!! This is an app which sits on your smartfone / tablet. You scan a QR code from a medicinal product and our app will verify if the product you have is genuine. It's simple, It's free.

The design could be very modern and simple. It should show in graphical form how the app works and have FAQ's etc.

pillcheckhub.net is designed specifically to allow consumers verify that the medical products which they have purchased are genuine.

Detailed brief with content attached. Logo in high res and QR code attached.

Full website required.
Updates

Target Market(s)

Pharmaceutical

Industry/Entity Type

Pharmaceutical

Coding

Coded - Design and coding required

Number of Pages Required

3 page

Colors

Designer to choose colors to be used in the design.

Requirements
Must have
• Strong visuals - very simple navigation - 3 pages
Nice to have
• Animation of the process
Should not have
• Jargon!

```html
<!DOCTYPE html>
<html lang="en">
<head>
<meta charset="utf-8">
<title>pillcheckhub.net</title>
<link href="https://fonts.googleapis.com/css2?family=Roboto:wght@400;500;700&family=PT+Sans:wght@400;700&display=swap" rel="stylesheet">
<style>
:root{
  --green:#4a9d3c;
  --blue:#2a6db0;
  --ink:#1b1b1b;
  --muted:#6f6f6f;
  --band:#f1f1f1;
  --footer:#121212;
  --white:#ffffff;
}
*{margin:0;padding:0;box-sizing:border-box}
html,body{width:757px;height:1200px;overflow:hidden;background:var(--white)}
body{position:relative;font-family:"PT Sans",sans-serif;color:var(--ink)}
.abs{position:absolute}
.center{text-align:center;left:0;width:757px}

/* hero */
.hero{position:absolute;left:0;top:0;width:757px;height:340px;
  background:linear-gradient(180deg,#6f7479 0%,#8d9095 45%,#7d8ea3 70%,#c9c9c4 100%)}
.hero-shade{position:absolute;inset:0;background:rgba(30,34,40,.38)}
.navbar{position:absolute;left:126px;top:27px;width:505px;height:59px;background:var(--white);
  display:flex;align-items:center;padding:0 10px 0 6px}
.brand{display:flex;flex-direction:column;align-items:center;gap:3px;font-family:"Roboto",sans-serif;font-size:8.5px;font-weight:500;color:var(--blue)}
.brand-dot{width:34px;height:34px;border-radius:50%;background:var(--green)}
.nav{margin-left:auto;display:flex;align-items:center;gap:0;font-family:"Roboto",sans-serif;font-size:8.5px;font-weight:500}
.nav a{text-decoration:none;color:var(--ink);margin-left:30px}
.nav a.active{color:var(--blue)}
.nav svg{margin-left:30px}
.hero-title{top:146px;font-family:"Roboto",sans-serif;font-weight:500;font-size:14.4px;line-height:23px;color:var(--white);text-transform:uppercase}
.hero-sub{top:202px;font-size:10.4px;color:var(--white)}
.btn{position:absolute;background:var(--green);color:var(--white);font-family:"Roboto",sans-serif;font-weight:500;
  display:flex;align-items:center;justify-content:center;text-transform:uppercase}
.btn-hero{left:325px;top:247px;width:107px;height:33px;font-size:11px}

/* steps */
.step{position:absolute;top:370px;width:180px;text-align:center}
.step-icon{width:54px;height:54px;border-radius:50%;background:#efefef;margin:0 auto;display:flex;align-items:center;justify-content:center}
.step h3{margin-top:26px;font-family:"Roboto",sans-serif;font-weight:500;font-size:10px;letter-spacing:.2px}
.step p{margin-top:6px;font-size:7.6px;line-height:13px;color:#333}

/* bands */
.band{position:absolute;left:0;width:757px;background:linear-gradient(120deg,#f6f6f6 0%,#ebebeb 50%,#f5f5f5 100%)}
.section-title{font-family:"Roboto",sans-serif;font-weight:500;font-size:14.4px;text-transform:uppercase}
.divider{position:absolute;left:310px;width:136px;height:20px}
.body-text{font-size:7.6px;line-height:13px;color:#333}
.btn-more{left:344px;top:663px;width:69px;height:23px;font-size:8px}

/* faq */
.faq{position:absolute;width:230px;display:flex;gap:10px}
.faq-plus{flex:none;width:22px;height:22px;background:var(--green);display:flex;align-items:center;justify-content:center}
.faq h4{font-family:"Roboto",sans-serif;font-weight:500;font-size:8.3px;margin-top:-1px;text-transform:uppercase}
.faq p{font-size:7.3px;line-height:11.5px;color:var(--muted);margin-top:3px}

/* footer */
.footer{position:absolute;left:0;top:1059px;width:757px;height:141px;background:var(--footer);color:var(--white)}
.f-head{position:absolute;top:23px;font-family:"Roboto",sans-serif;font-weight:500;font-size:11.5px}
.f-rule{position:absolute;top:45px;height:1px;background:#777}
.f-rule span{display:block;width:28px;height:2px;margin-top:-1px;background:var(--blue)}
.socials{position:absolute;left:126px;top:58px;display:flex;gap:6px}
.socials span{width:19px;height:19px;border-radius:50%;background:var(--blue)}
.f-small{font-size:7.4px;line-height:12.5px}
.contact{position:absolute;left:331px;display:flex;gap:10px;align-items:flex-start}
.links{position:absolute;left:555px;top:61px;list-style:none;font-size:7.6px;line-height:15.3px}
</style>
</head>
<body>

<header class="hero" role="img" aria-label="Photo of colourful capsules and white tablets scattered on a pharmacy table">
  <div class="hero-shade"></div>
</header>
<nav class="navbar">
  <div class="brand"><span class="brand-dot"></span>pillcheckhub.net</div>
  <div class="nav">
    <a class="active">HOME</a><a>ABOUT US</a><a>FAQ</a>
    <svg width="10" height="10" viewBox="0 0 10 10"><circle cx="4" cy="4" r="3" fill="none" stroke="#1b1b1b" stroke-width="1.6"/><line x1="6.2" y1="6.2" x2="9.2" y2="9.2" stroke="#1b1b1b" stroke-width="1.8"/></svg>
  </div>
</nav>
<h1 class="abs center hero-title">30% of all medicine bought online is counterfeitare you sure<br>that the medication you take is genuine?</h1>
<p class="abs center hero-sub">Be Safe, AuthenticateProtect your health with pillcheckhub</p>
<a class="btn btn-hero">Download App</a>

<section>
  <div class="step" style="left:92px">
    <div class="step-icon"><svg width="30" height="28" viewBox="0 0 30 28"><path d="M12 2h6v9h5l-8 8-8-8h5z" fill="#4a9d3c"/><path d="M2 17v9h26v-9" fill="none" stroke="#4a9d3c" stroke-width="3"/></svg></div>
    <h3>DOWNLOAD OUR APP</h3>
    <p>Lorem Ipsum is simply dummy<br>text of the printing &amp; typesetting</p>
  </div>
  <div class="step" style="left:288px">
    <div class="step-icon"><svg width="28" height="28" viewBox="0 0 28 28"><circle cx="11" cy="11" r="8" fill="none" stroke="#4a9d3c" stroke-width="2.6"/><rect x="7.5" y="7.5" width="7" height="7" fill="none" stroke="#4a9d3c" stroke-width="1.4"/><line x1="17" y1="17" x2="25" y2="25" stroke="#4a9d3c" stroke-width="3.4" stroke-linecap="round"/></svg></div>
    <h3>SCAN &nbsp;OR CODE</h3>
    <p>Lorem Ipsum is simply dummy<br>text of the printing &amp; typesetting</p>
  </div>
  <div class="step" style="left:483px">
    <div class="step-icon"><svg width="30" height="26" viewBox="0 0 30 26"><path d="M2 18a8 8 0 0 1 16 0z" fill="#4a9d3c"/><path d="M2 20h16a8 8 0 0 1-16 0z" fill="#4a9d3c"/><rect x="17" y="1" width="9" height="22" rx="4.5" transform="rotate(-35 21.5 12)" fill="#4a9d3c"/></svg></div>
    <h3>FIND MEDICINE</h3>
    <p>Lorem Ipsum is simply dummy<br>text of the printing &amp; typesetting</p>
  </div>
</section>

<section class="band" style="top:521px;height:186px">
  <h2 class="abs center section-title" style="top:29px">How does it work?</h2>
  <svg class="divider" style="top:50px" viewBox="0 0 136 20"><line x1="0" y1="10" x2="48" y2="10" stroke="#555"/><line x1="88" y1="10" x2="136" y2="10" stroke="#555"/><circle cx="64" cy="8" r="6" fill="#2a6db0"/><circle cx="72" cy="13" r="6" fill="#2a6db0" stroke="#f2f2f2" stroke-width="1.5"/></svg>
  <p class="abs center body-text" style="top:84px;left:136px;width:485px">Each time a pharmaceutical company produces medicine, they communicate with our Blockchain database and request a unique QR code from us. &nbsp;This unique QR code is printed on the foil/packaging for the medicine.When you receive your medicine, simply scan the QR code with your phone or tablet using your pillcheckhub app.</p>
</section>
<a class="btn btn-more">Read More</a>

<section>
  <h2 class="abs center section-title" style="top:741px">Frequently Asked Questions</h2>
  <svg class="divider" style="top:764px" viewBox="0 0 136 20"><line x1="0" y1="10" x2="48" y2="10" stroke="#555"/><line x1="88" y1="10" x2="136" y2="10" stroke="#555"/><circle cx="64" cy="8" r="6" fill="#2a6db0"/><circle cx="72" cy="13" r="6" fill="#2a6db0" stroke="#fff" stroke-width="1.5"/></svg>
  <div class="faq" style="left:126px;top:812px">
    <span class="faq-plus"><svg width="12" height="12"><path d="M6 0v12M0 6h12" stroke="#fff" stroke-width="2.4"/></svg></span>
    <div><h4>Can customers validate their medicine?</h4><p>Yes. Using our patented mobile application, can verify the authenticity of their medication</p></div>
  </div>
  <div class="faq" style="left:405px;top:812px;width:240px">
    <span class="faq-plus"><svg width="12" height="12"><path d="M6 0v12M0 6h12" stroke="#fff" stroke-width="2.4"/></svg></span>
    <div><h4>Can pillcheckhub do offline validation?</h4><p>Yes, PillCheckHub can validate medication even offline</p></div>
  </div>
  <div class="faq" style="left:126px;top:870px">
    <span class="faq-plus"><svg width="12" height="12"><path d="M6 0v12M0 6h12" stroke="#fff" stroke-width="2.4"/></svg></span>
    <div><h4>How much does it cost to validate my meds</h4><p>It's absolutely and forever free!</p></div>
  </div>
  <div class="faq" style="left:405px;top:870px">
    <span class="faq-plus"><svg width="12" height="12"><path d="M6 0v12M0 6h12" stroke="#fff" stroke-width="2.4"/></svg></span>
    <div><h4>I'm a pharmacy/retailer, how can ....</h4><p>Please contact us at info@pillcheckhub.net</p></div>
  </div>
</section>

<section class="band" style="top:929px;height:130px">
  <h2 class="abs center section-title" style="top:31px">Medicine Authenticity Guaranteed</h2>
  <svg class="divider" style="top:53px" viewBox="0 0 136 20"><line x1="0" y1="10" x2="48" y2="10" stroke="#555"/><line x1="88" y1="10" x2="136" y2="10" stroke="#555"/><circle cx="64" cy="8" r="6" fill="#2a6db0"/><circle cx="72" cy="13" r="6" fill="#2a6db0" stroke="#f2f2f2" stroke-width="1.5"/></svg>
  <p class="abs center body-text" style="top:85px">Medicine Authenticity will be guaranteed by an end-to-end Verification System. Each step is logged and end customers<br>can validate the authenticity of their pills</p>
</section>

<footer class="footer">
  <div class="f-head" style="left:126px;font-size:12px">PILLCHECKHUB</div>
  <div class="socials"><span></span><span></span><span></span><span></span></div>
  <p class="abs f-small" style="left:126px;top:85px">© Copyright 2017 pillcheckhub.<br>All Rights Reserved.</p>

  <div class="f-head" style="left:331px">Keep in Touch</div>
  <div class="f-rule" style="left:331px;width:102px"><span></span></div>
  <div class="contact f-small" style="top:62px">
    <svg width="10" height="10" viewBox="0 0 10 10"><path d="M2 0l2 2.5-1.2 1.3a6 6 0 0 0 3.4 3.4L7.5 6 10 8 8.5 10C4 10 0 6 0 1.5z" fill="#2a6db0"/></svg>
    <span>+1234567891</span>
  </div>
  <div class="contact f-small" style="top:81px">
    <svg width="10" height="12" viewBox="0 0 10 12"><path d="M5 0a4.5 4.5 0 0 1 4.5 4.5C9.5 8 5 12 5 12S.5 8 .5 4.5A4.5 4.5 0 0 1 5 0z" fill="#2a6db0"/><circle cx="5" cy="4.5" r="1.6" fill="#121212"/></svg>
    <span>Lorem Ipsum is simply dummy text<br>of the printing</span>
  </div>
  <div class="contact f-small" style="top:114px">
    <svg width="11" height="9" viewBox="0 0 11 9"><rect width="11" height="9" fill="#2a6db0"/><path d="M0 0l5.5 5L11 0" fill="none" stroke="#121212"/></svg>
    <span>info@pillcheckhub.net</span>
  </div>

  <div class="f-head" style="left:549px">Quick Links</div>
  <div class="f-rule" style="left:549px;width:81px"><span></span></div>
  <ul class="links"><li>Home</li><li>About us</li><li>FAQ</li><li>Help</li></ul>
</footer>

</body>
</html>
```